New Crowdfunding site Fundlark needs banner ads

I’m looking for 4 standard size banner ads for www.fundlark.example to be used by LinkaDeal Affiliates in order to bring new crowdfunding projects to the platform.
728x90
160x600
300x250
180x160

Succesful designers will put on our Mentors list so that the project owner can also get their specific project banners from our designers. Designers can also become our affiliates either to promote Fundlark.example or individual projects.
Updates

Please note updated brief

Thank you to those that have submitted designs so far.
Please be reminded that the invitation will close tomorrow after which we will make our choice

Thanks for input so far.
Please note project closes tomorrow (Sunday) after which we will choose.

Target Market(s)

Target is a project owner with a project requiring $10,000 or more in any field including business and/or non-profits. Any country.
Inventors, creatives, communities, hardware or software, consumer items,

Industry/Entity Type

Crowdfunding

Font styles to use
Sans Serif

Requirements
Must have
• Clear button call to action based on our USPs shown on the home page but especially the use of Affiliate Networks to promote their project to the widest possible audience.

Text and button text should be editable (see png preference).
Call to action could be based on "Free Crowdfunding Consultation - is your project viable" or "Get Your Free Guide to Succesful Crowdfunding"
Nice to have
• .png format preferred with separate objects.
Some animation preferred in the button.

```html
<!DOCTYPE html>
<html lang="en">
<head>
<meta charset="utf-8">
<title>Fundlark banner set</title>
<link rel="stylesheet" href="https://fonts.googleapis.com/css2?family=Oswald:wght@400;500&family=Open+Sans:wght@400;600&display=swap">
<style>
  :root {
    --backdrop: #3a1a0e;
    --navy: #13497e;
    --navy-deep: #0d3a66;
    --green: #16b815;
    --green-edge: #0e9a0e;
    --white: #ffffff;
    --ink: #111111;
    --funding-blue: #1f1fe0;
    --photo-light: #dfe7ee;
    --photo-mid: #9fb8d0;
    --rule: rgba(255,255,255,0.35);
  }
  * { box-sizing: border-box; margin: 0; padding: 0; }
  html, body { width: 1200px; height: 1109px; overflow: hidden; }
  body { background: var(--backdrop); position: relative; font-family: "Oswald", sans-serif; }

  .banner { position: absolute; overflow: hidden; background: var(--navy); box-shadow: 0 2px 6px rgba(0,0,0,.45); }
  .leaderboard { left: 78px; top: 81px; width: 1000px; height: 122px; }
  .skyscraper { left: 78px; top: 224px; width: 220px; height: 823px; }
  .rectangle { left: 317px; top: 224px; width: 413px; height: 342px; }
  .square { left: 317px; top: 601px; width: 247px; height: 221px; }

  .block { position: absolute; }
  .white-panel { background: var(--white); }
  .navy-panel { background: linear-gradient(180deg, var(--navy) 0%, var(--navy-deep) 100%); color: var(--white); text-align: center; }
  .green-panel { background: var(--green); border: 1px solid var(--green-edge); color: var(--ink); display: flex; align-items: center; justify-content: center; text-align: center; }
  .photo { background: linear-gradient(135deg, var(--photo-light) 0%, var(--photo-mid) 100%); }

  .brand { font-family: "Open Sans", sans-serif; font-weight: 600; color: var(--navy); display: flex; align-items: center; gap: 8px; justify-content: center; }
  .brand-dot { border-radius: 50%; background: var(--navy); flex: none; }

  .formula { font-family: "Oswald", sans-serif; color: var(--navy); line-height: 1.2; }
  .formula .funding { color: var(--funding-blue); }
  .formula.light { color: var(--white); }
  .formula.light .funding { color: var(--white); }

  .headline { font-weight: 500; line-height: 1.05; text-transform: uppercase; }
  .subline { font-family: "Open Sans", sans-serif; line-height: 1.2; text-transform: uppercase; }
  .cta { font-weight: 400; line-height: 1.2; text-transform: uppercase; }
  .cta svg { vertical-align: -2px; margin-right: 6px; }

  .site { font-family: "Open Sans", sans-serif; color: var(--white); background: var(--navy-deep); display: flex; align-items: center; justify-content: center; }
  .notch-right { position: absolute; width: 0; height: 0; border-top: 12px solid transparent; border-bottom: 12px solid transparent; border-left: 12px solid var(--navy-deep); }
  .notch-down { position: absolute; width: 0; height: 0; border-left: 12px solid transparent; border-right: 12px solid transparent; border-top: 12px solid var(--navy-deep); }
</style>
</head>
<body>

<svg width="0" height="0" style="position:absolute">
  <symbol id="chevron-badge" viewBox="0 0 16 16">
    <circle cx="8" cy="8" r="8" fill="#111"/>
    <path d="M6.5 4.5 10 8 6.5 11.5" fill="none" stroke="#fff" stroke-width="2"/>
  </symbol>
</svg>

<!-- 728x90 -->
<section class="banner leaderboard">
  <div class="block white-panel" style="left:0;top:0;width:238px;height:122px;">
    <div class="brand" style="position:absolute;top:20px;left:0;width:238px;font-size:30px;"><span class="brand-dot" style="width:22px;height:22px;"></span>Fundlark</div>
    <div class="formula" style="position:absolute;top:82px;left:0;width:238px;text-align:center;font-size:17px;">PROJECT + CROWD = <span class="funding">FUNDING</span></div>
  </div>
  <div class="block photo" role="img" aria-label="Photo of a smiling businessman at a desk with a laptop" style="left:241px;top:0;width:234px;height:122px;"></div>
  <div class="block navy-panel" style="left:475px;top:0;width:306px;height:122px;padding-top:8px;">
    <div class="headline" style="font-size:35px;">Free Consultation</div>
    <div class="subline" style="font-size:17px;margin-top:8px;">Every new project gets 2<br>hours of one on one help</div>
  </div>
  <div class="notch-right" style="left:781px;top:49px;"></div>
  <div class="block green-panel" style="left:781px;top:0;width:219px;height:122px;">
    <div class="cta" style="font-size:21px;"><svg width="18" height="18"><use href="#chevron-badge"/></svg>Get your free<br>guide to succesful<br>crowdfunding</div>
  </div>
</section>

<!-- 160x600 -->
<section class="banner skyscraper">
  <div class="block white-panel" style="left:0;top:0;width:220px;height:95px;">
    <div class="brand" style="position:absolute;top:30px;left:0;width:220px;font-size:30px;"><span class="brand-dot" style="width:22px;height:22px;"></span>Fundlark</div>
  </div>
  <div class="block photo" role="img" aria-label="Photo of a smiling businessman at a desk with a laptop" style="left:0;top:95px;width:220px;height:277px;"></div>
  <div class="block navy-panel" style="left:0;top:372px;width:220px;height:295px;padding-top:24px;">
    <div class="formula light" style="font-size:24px;">PROJECT + CROWD<br>=<span class="funding">FUNDING</span></div>
    <div style="height:1px;background:var(--rule);margin:16px 14px 18px;"></div>
    <div class="headline" style="font-size:35px;">Free<br>Consultation</div>
    <div class="subline" style="font-size:19px;margin-top:6px;">Every new project<br>gets 2 hours of<br>one on one help</div>
  </div>
  <div class="notch-down" style="left:98px;top:667px;z-index:1;"></div>
  <div class="block green-panel" style="left:0;top:667px;width:220px;height:125px;">
    <div class="cta" style="font-size:21px;"><svg width="18" height="18"><use href="#chevron-badge"/></svg>Get your free<br>guide to succesful<br>crowdfunding</div>
  </div>
  <div class="block site" style="left:0;top:792px;width:220px;height:31px;font-size:15px;">www.fundlark.example</div>
</section>

<!-- 300x250 -->
<section class="banner rectangle">
  <div class="block white-panel" style="left:0;top:0;width:413px;height:95px;">
    <div class="brand" style="position:absolute;top:30px;left:0;width:215px;font-size:30px;"><span class="brand-dot" style="width:22px;height:22px;"></span>Fundlark</div>
    <div class="formula" style="position:absolute;top:16px;left:215px;width:198px;text-align:center;font-size:24px;">PROJECT + CROWD<br>=<span class="funding">FUNDING</span></div>
  </div>
  <div class="block navy-panel" style="left:0;top:95px;width:215px;height:166px;padding:12px 0 0 18px;text-align:left;">
    <div class="headline" style="font-size:30px;">Free<br>Consultation</div>
    <div style="height:1px;background:var(--rule);margin:6px 14px 8px 0;"></div>
    <div class="subline" style="font-size:17px;">Every new project<br>gets 2 hours of<br>one on one help</div>
  </div>
  <div class="notch-right" style="left:215px;top:150px;z-index:1;"></div>
  <div class="block photo" role="img" aria-label="Photo of a smiling businessman at a desk with a laptop" style="left:215px;top:95px;width:198px;height:247px;"></div>
  <div class="block green-panel" style="left:0;top:261px;width:215px;height:55px;">
    <div class="cta" style="font-size:16px;"><svg width="14" height="14"><use href="#chevron-badge"/></svg>Get your free guide to<br>succesful crowdfunding</div>
  </div>
  <div class="block site" style="left:0;top:316px;width:215px;height:26px;font-size:13px;">www.fundlark.example</div>
</section>

<!-- 180x150 -->
<section class="banner square">
  <div class="block white-panel" style="left:0;top:0;width:247px;height:50px;">
    <div class="brand" style="position:absolute;top:13px;left:0;width:128px;font-size:18px;gap:5px;"><span class="brand-dot" style="width:14px;height:14px;"></span>Fundlark</div>
    <div class="formula" style="position:absolute;top:8px;left:128px;width:119px;text-align:center;font-size:14px;">PROJECT + CROWD<br>=<span class="funding">FUNDING</span></div>
  </div>
  <div class="block navy-panel" style="left:0;top:50px;width:247px;height:120px;padding-top:12px;">
    <div class="headline" style="font-size:29px;">Free Consultation</div>
    <div class="subline" style="font-size:15px;margin-top:16px;">Every new project gets<br>2 hours of one on one help</div>
  </div>
  <div class="block green-panel" style="left:0;top:170px;width:247px;height:51px;">
    <div class="cta" style="font-size:16px;"><svg width="13" height="13"><use href="#chevron-badge"/></svg>Get your free guide to<br>succesful crowdfunding</div>
  </div>
</section>

</body>
</html>
```